Business Card design for a skin clinic

i would like a business card design for our skin clinic.
our logo colors are Blue and Grey and Bule /white.
we are searching for a minimalistic design yet very elegant,dynamic and professional which can reflect a professional medical skin care clinic( not a beauty salon).
THE DESGIN IS NOT FOR A PERSON IT WILL BE USED IN THE CLINIC FOR CLIENTS SO THERE SHOULD BE NO NAME OF A PERSON ONLY THE CLINIC NAME AND THE CONTACT INFO

Target Market(s)
young and old womens
Industry/Entity Type
Business
Contact Information for Business Card
we have 2 address and both should be on the card.
address A: Lindenhoflaan 214B, 3041KP Rotterdam, Tel 010 483 21 95
address B: Zonnewijzerstraat 238, 1062RT Amsterdam Tel 020 571 3829
website www.huidpuntzorg.nu, email info@huidpuntzorg.nu
Look and feel
Each slider illustrates characteristics of the customer's brand and the style your logo design should communicate.

```html
<!DOCTYPE html>
<html lang="nl">
<head>
<meta charset="utf-8">
<title>Huidpuntzorg – visitekaartje</title>
<link rel="stylesheet" href="https://fonts.googleapis.com/css2?family=Encode+Sans+Condensed:wght@400&family=Montserrat:wght@400&display=swap">
<style>
  :root {
    --page-bg: #ffffff;
    --card-white: #ffffff;
    --brand-blue: #388fcb;
    --brand-grey: #5f5f62;
    --text-light: #ffffff;
    --shadow: rgba(0, 0, 0, 0.16);
  }
  * { margin: 0; padding: 0; box-sizing: border-box; }
  html, body {
    width: 1200px;
    height: 1200px;
    overflow: hidden;
    background: var(--page-bg);
  }
  .canvas {
    position: relative;
    width: 1200px;
    height: 1200px;
  }
  .card {
    position: absolute;
    left: 203px;
    width: 794px;
    height: 520px;
    box-shadow: 0 6px 28px var(--shadow);
  }
  .card--front {
    top: 68px;
    background: var(--card-white);
  }
  .card--back {
    top: 606px;
    background: var(--brand-blue);
    color: var(--text-light);
    font-family: "Encode Sans Condensed", "Arial Narrow", sans-serif;
    font-size: 25px;
    line-height: 30px;
  }
  .brand {
    position: absolute;
    left: 0;
    right: 0;
    top: 260px;
    text-align: center;
  }
  .brand__name {
    font-family: "Encode Sans Condensed", "Arial Narrow", sans-serif;
    font-weight: 400;
    font-size: 52px;
    letter-spacing: 7px;
    color: var(--brand-blue);
    line-height: 1;
  }
  .brand__tagline {
    margin-top: 22px;
    font-family: "Montserrat", sans-serif;
    font-size: 14px;
    letter-spacing: 2.4px;
    color: var(--brand-grey);
    text-transform: lowercase;
  }
  .contact {
    position: absolute;
    left: 455px;
    top: 112px;
  }
  .contact__location + .contact__location { margin-top: 23px; }
  .contact__online { margin-top: 20px; }
  .contact__row {
    display: flex;
    align-items: center;
    gap: 14px;
  }
  .contact__row + .contact__row { margin-top: 10px; }
  .contact__icon {
    width: 28px;
    height: 28px;
    flex: none;
  }
</style>
</head>
<body>
<main class="canvas">
  <section class="card card--front" aria-label="Voorkant">
    <div class="brand">
      <div class="brand__name">HUIDPUNTZORG</div>
      <div class="brand__tagline">next generation skin care</div>
    </div>
  </section>

  <section class="card card--back" aria-label="Achterkant">
    <div class="contact">
      <address class="contact__location" style="font-style:normal">
        Lindenhoflaan 214B,<br>
        3041KP Rotterdam,<br>
        P: 010 483 21 95
      </address>
      <address class="contact__location" style="font-style:normal">
        Zonnewijzerstraat 238,<br>
        1062RT Amsterdam<br>
        P: 020 571 3829
      </address>
      <div class="contact__online">
        <div class="contact__row">
          <svg class="contact__icon" viewBox="0 0 28 28" fill="none" stroke="#fff" stroke-width="1.6">
            <rect x="1.5" y="7" width="25" height="15"/>
            <path d="M1.5 7 L14 16 L26.5 7"/>
            <path d="M1.5 22 L11 14.5 M26.5 22 L17 14.5"/>
          </svg>
          <span>info@huidpuntzorg.nu</span>
        </div>
        <div class="contact__row">
          <svg class="contact__icon" viewBox="0 0 28 28" fill="none" stroke="#fff" stroke-width="1.4">
            <circle cx="13" cy="13" r="11"/>
            <ellipse cx="13" cy="13" rx="5" ry="11"/>
            <path d="M2 13 H24 M4 7 H22 M4 19 H22 M13 2 V24"/>
            <path d="M18 17 L26 21 L22 22 L20 26 Z" fill="#fff"/>
          </svg>
          <span>www.huidpuntzorg.nu</span>
        </div>
      </div>
    </div>
  </section>
</main>
</body>
</html>
```